Worksheet for a seminar - wheel of wellbeing

I need a 1 page worksheet for a course I am running next week.
1. The worksheet is based is designed to tie into Valdoric who use 4 colours per specific quadrants - Blue top left, Yellow top right, Green bottom left, Red bottom right. As this is designed to be written and to be printed, it may need to be pale colours however I am open to the correct colours with the image on top if necessary

2. The wellbeing wheel needs to be a design of it's own as it will be used in other things. I would like to have a format for the base wheel that can be changed by me (Only the title names)

3. I have provided the 2 business logo's - these down need to be too big

I hope this helps.

Target Market(s)

Corporate managers and staff - worksheet being used in a workshop

Industry/Entity Type

Wheel

Colors

Designer to choose colors to be used in the design.

Requirements
Must have
• A professional looking wheel that can be used for other purposes. I want to be able to change the 'pie' titles. I will also require a A4 size of the wheel with blank spaces for titles
Nice to have
• A modern feel

```html
<!DOCTYPE html>
<html lang="en">
<head>
<meta charset="utf-8">
<title>Wheel of Well Being – Worksheet</title>
<link href="https://fonts.googleapis.com/css2?family=Montserrat:wght@400;500;600;700;800;900&display=swap" rel="stylesheet">
<style>
  :root{
    --ink:#1f1f1f;
    --title-blue:#1b8fd2;
    --assess-orange:#f07d1a;
    --band-dark:#1e1e1e;
    --stripe-yellow:#ffc400;
    --stripe-orange:#ff8a00;
    --stripe-deep:#f36b12;
    --panel-assess:#d5ebf7;
    --panel-goals:#f8efe2;
    --panel-action:#d7ead2;
    --panel-reflect:#f2cccc;
    --field:#f1f1f1;
    --field-ghost:#e2e2e2;
    --footer:#f0f0f0;
    --brand-green:#5aa632;
    --brand-teal:#3aa68e;
  }
  *{box-sizing:border-box;margin:0;padding:0}
  html,body{width:950px;height:1200px;overflow:hidden;background:#fff}
  body{font-family:"Montserrat",sans-serif;color:var(--ink)}
  .sheet{position:relative;width:950px;height:1200px;background:#fff;overflow:hidden}

  .header-art{position:absolute;left:0;top:0}
  .title{position:absolute;left:260px;top:20px;width:680px;text-align:center}
  .title h1{font-weight:900;font-size:70px;letter-spacing:1px;color:var(--title-blue);line-height:1}
  .title p{font-weight:500;font-size:33px;letter-spacing:.5px;margin-top:8px;line-height:1}

  .col-head{position:absolute;top:208px}
  .col-head h2{font-weight:800;font-size:25px;line-height:1.1}
  .col-head p{font-size:20px;font-weight:500;margin-top:4px}
  .col-head.assess{left:30px}
  .col-head.assess h2{color:var(--assess-orange)}
  .col-head.goals{left:505px}
  .col-head.goals h2{color:var(--title-blue)}

  .panel{position:absolute;width:475px}
  .panel.assess{left:0;top:269px;height:461px;background:var(--panel-assess)}
  .panel.goals{left:475px;top:269px;height:461px;background:var(--panel-goals)}
  .panel.action{left:0;top:730px;height:327px;background:var(--panel-action)}
  .panel.reflect{left:475px;top:730px;height:327px;background:var(--panel-reflect)}

  .wheel{position:absolute;left:28px;top:16px;width:420px;height:420px}
  .wheel-label{font-family:"Montserrat",sans-serif;font-size:11px;font-weight:600;fill:#fff}
  .date{position:absolute;left:32px;top:433px;font-size:16px;font-weight:500}

  .panel h3{position:absolute;left:32px;top:16px;font-size:19px;font-weight:700;color:var(--title-blue)}
  .reflect h3{left:15px}
  .plan-row{position:absolute;left:30px;width:420px;height:53px}
  .plan-row .field{position:absolute;top:0;height:53px;background:var(--field);border-radius:8px;
    display:flex;align-items:center;justify-content:center;color:var(--field-ghost);font-weight:700;font-size:16px}
  .plan-row .act{left:0;width:267px}
  .plan-row .when{left:274px;width:146px}
  .plan-row .num{position:absolute;left:6px;top:6px;font-size:34px;font-weight:800;color:var(--field-ghost)}

  .question{position:absolute;left:15px;font-size:15px;font-weight:500}
  .answer{position:absolute;left:15px;width:420px;height:38px;background:#fff;border-radius:9px}

  .footer{position:absolute;left:0;top:1057px;width:950px;height:143px;background:var(--footer)}
  .brand{position:absolute;display:flex;align-items:center;gap:12px;font-weight:800;font-size:44px;line-height:1}
  .brand.rise{left:110px;top:48px;color:var(--brand-green)}
  .brand.calm{left:560px;top:52px;color:var(--brand-teal);font-size:36px}
  .brand .mark{display:block;border-radius:50%}
  .brand.rise .mark{width:30px;height:30px;background:var(--brand-green)}
  .brand.calm .mark{width:24px;height:24px;background:var(--brand-teal)}
  .footer-art{position:absolute;left:0;top:0}
</style>
</head>
<body>
<main class="sheet">

  <svg class="header-art" width="950" height="200" viewBox="0 0 950 200" aria-hidden="true">
    <polygon points="0,0 40,0 40,0 0,0" fill="none"/>
    <polygon points="0,10 50,10 140,140 0,140" fill="var(--stripe-deep)"/>
    <polygon points="0,60 70,60 110,118 0,118" fill="var(--stripe-orange)"/>
    <polygon points="0,0 85,0 210,178 140,178 0,0" fill="var(--band-dark)"/>
    <polygon points="85,0 145,0 270,178 210,178" fill="var(--stripe-yellow)"/>
    <polygon points="145,0 160,0 285,178 270,178" fill="var(--stripe-orange)"/>
    <rect x="140" y="144" width="810" height="34" fill="var(--band-dark)"/>
    <path d="M428 178 A48 40 0 0 0 524 178 Z" fill="var(--band-dark)"/>
    <polyline points="462,183 476,192 490,183" fill="none" stroke="var(--stripe-orange)" stroke-width="2"/>
    <polygon points="900,0 950,0 950,52" fill="var(--title-blue)"/>
  </svg>

  <header class="title">
    <h1>WHEEL OF WELL</h1>
    <p>BEING A WHOLE BRAIN APPROACH</p>
  </header>

  <div class="col-head assess"><h2>ASSESS</h2><p>Where are You Now?</p></div>
  <div class="col-head goals"><h2>OUTCOMES / GOALS</h2><p>Where do you want to be?</p></div>

  <svg width="0" height="0" style="position:absolute" aria-hidden="true">
    <defs>
      <path id="arc-1" d="M225 28.1 A192 192 0 0 1 352.2 80.7"/>
      <path id="arc-2" d="M359.3 87.9 A192 192 0 0 1 411.9 215"/>
      <path id="arc-3" d="M411.9 225 A192 192 0 0 1 359.3 352.1"/>
      <path id="arc-4" d="M352.2 359.3 A192 192 0 0 1 225 411.9"/>
      <path id="arc-4r" d="M225 411.9 A192 192 0 0 0 352.2 359.3"/>
      <path id="arc-5" d="M215 411.9 A192 192 0 0 1 87.8 359.3"/>
      <path id="arc-5r" d="M87.8 359.3 A192 192 0 0 0 215 411.9"/>
      <path id="arc-6" d="M80.7 352.2 A192 192 0 0 1 28.1 225"/>
      <path id="arc-7" d="M28.1 215 A192 192 0 0 1 80.7 87.8"/>
      <path id="arc-8" d="M87.8 80.7 A192 192 0 0 1 215 28.1"/>
      <path id="slice-1" d="M220 220 L220 50 A170 170 0 0 1 340.2 99.8 Z"/>
      <path id="slice-2" d="M220 220 L340.2 99.8 A170 170 0 0 1 390 220 Z"/>
      <path id="slice-3" d="M220 220 L390 220 A170 170 0 0 1 340.2 340.2 Z"/>
      <path id="slice-4" d="M220 220 L340.2 340.2 A170 170 0 0 1 220 390 Z"/>
      <path id="slice-5" d="M220 220 L220 390 A170 170 0 0 1 99.8 340.2 Z"/>
      <path id="slice-6" d="M220 220 L99.8 340.2 A170 170 0 0 1 50 220 Z"/>
      <path id="slice-7" d="M220 220 L50 220 A170 170 0 0 1 99.8 99.8 Z"/>
      <path id="slice-8" d="M220 220 L99.8 99.8 A170 170 0 0 1 220 50 Z"/>
    </defs>
  </svg>

  <section class="panel assess">
    <svg class="wheel" viewBox="0 0 440 440" role="img" aria-label="Wellbeing wheel with eight areas">
      <g stroke="var(--panel-assess)" stroke-width="5" stroke-linejoin="round">
        <use href="#slice-1" fill="#dcbc66"/><use href="#slice-2" fill="#c6dba8"/>
        <use href="#slice-3" fill="#c9a088"/><use href="#slice-4" fill="#c4dc7c"/>
        <use href="#slice-5" fill="#d99c9c"/><use href="#slice-6" fill="#c498c4"/>
        <use href="#slice-7" fill="#e3c9b8"/><use href="#slice-8" fill="#58a0bf"/>
      </g>
      <g fill="none" stroke-width="22">
        <use href="#arc-1" stroke="#a59a5a"/><use href="#arc-2" stroke="#1e7a3a"/>
        <use href="#arc-3" stroke="#172a5e"/><use href="#arc-4" stroke="#6b6658"/>
        <use href="#arc-5" stroke="#b0561e"/><use href="#arc-6" stroke="#c7a23a"/>
        <use href="#arc-7" stroke="#a6822a"/><use href="#arc-8" stroke="#b866d6"/>
      </g>
      <g class="wheel-label" text-anchor="middle" dominant-baseline="central">
        <text><textPath href="#arc-1" startOffset="50%">Physical Health</textPath></text>
        <text><textPath href="#arc-2" startOffset="50%">Emotional Health</textPath></text>
        <text><textPath href="#arc-3" startOffset="50%">Spiritual</textPath></text>
        <text font-size="10"><textPath href="#arc-4r" startOffset="50%">Love / Relationship</textPath></text>
        <text><textPath href="#arc-5r" startOffset="50%">Family</textPath></text>
        <text><textPath href="#arc-6" startOffset="50%">SOCIAL</textPath></text>
        <text><textPath href="#arc-7" startOffset="50%">Personal Growth</textPath></text>
        <text font-size="9.5"><textPath href="#arc-8" startOffset="50%">Business Carrer Study</textPath></text>
      </g>
    </svg>
    <p class="date">Date :</p>
  </section>

  <section class="panel goals">
    <svg class="wheel" viewBox="0 0 440 440" role="img" aria-label="Blank goals wheel with eight areas">
      <g stroke="var(--panel-goals)" stroke-width="5" stroke-linejoin="round">
        <use href="#slice-1" fill="#fbe9b8"/><use href="#slice-2" fill="#d8e8c4"/>
        <use href="#slice-3" fill="#f5cdbd"/><use href="#slice-4" fill="#a9c8b2"/>
        <use href="#slice-5" fill="#ebbcc2"/><use href="#slice-6" fill="#dcbcdc"/>
        <use href="#slice-7" fill="#ddd4cc"/><use href="#slice-8" fill="#b2e0f2"/>
      </g>
      <g fill="none" stroke-width="22">
        <use href="#arc-1" stroke="#a59a5a"/><use href="#arc-2" stroke="#1e7a3a"/>
        <use href="#arc-3" stroke="#172a5e"/><use href="#arc-4" stroke="#6b6658"/>
        <use href="#arc-5" stroke="#b0561e"/><use href="#arc-6" stroke="#c7a23a"/>
        <use href="#arc-7" stroke="#a6822a"/><use href="#arc-8" stroke="#b866d6"/>
      </g>
      <g class="wheel-label" text-anchor="middle" dominant-baseline="central">
        <text><textPath href="#arc-1" startOffset="50%">TEXT HERE</textPath></text>
        <text><textPath href="#arc-2" startOffset="50%">TEXT HERE</textPath></text>
        <text><textPath href="#arc-3" startOffset="50%">TEXT HERE</textPath></text>
        <text><textPath href="#arc-4" startOffset="50%">TEXT HERE</textPath></text>
        <text><textPath href="#arc-5" startOffset="50%">TEXT HERE</textPath></text>
        <text><textPath href="#arc-6" startOffset="50%">TEXT HERE</textPath></text>
        <text><textPath href="#arc-7" startOffset="50%">TEXT HERE</textPath></text>
        <text><textPath href="#arc-8" startOffset="50%">TEXT HERE</textPath></text>
      </g>
    </svg>
    <p class="date">Date Achieved By :</p>
  </section>

  <section class="panel action">
    <h3>Action Plan</h3>
    <div class="plan-row" style="top:50px"><div class="field act">Action</div><span class="num">1</span><div class="field when">When</div></div>
    <div class="plan-row" style="top:119px"><div class="field act">Action</div><span class="num">2</span><div class="field when">When</div></div>
    <div class="plan-row" style="top:188px"><div class="field act">Action</div><span class="num">3</span><div class="field when">When</div></div>
    <div class="plan-row" style="top:257px"><div class="field act">Action</div><span class="num">4</span><div class="field when">When</div></div>
  </section>

  <section class="panel reflect">
    <h3>Reflect</h3>
    <p class="question" style="top:50px">Are there any surprised in your Wheel?</p>
    <div class="answer" style="top:76px"></div>
    <p class="question" style="top:118px;font-size:14px">What wellbeing gaps stand out as being most&nbsp; importang?.</p>
    <div class="answer" style="top:143px"></div>
    <p class="question" style="top:186px">How do you feel about it ?</p>
    <div class="answer" style="top:211px"></div>
    <p class="question" style="top:252px">How might this affect your homelife / worklife ?</p>
    <div class="answer" style="top:277px"></div>
  </section>

  <footer class="footer">
    <svg class="footer-art" width="950" height="143" viewBox="0 0 950 143" aria-hidden="true">
      <polygon points="0,80 0,143 45,143" fill="var(--stripe-yellow)"/>
      <polygon points="0,110 0,143 22,143" fill="var(--stripe-orange)"/>
      <polygon points="950,40 950,143 870,143" fill="var(--band-dark)"/>
      <polygon points="900,80 870,143 845,143" fill="var(--stripe-yellow)"/>
      <polygon points="950,100 950,143 915,143" fill="var(--stripe-orange)"/>
    </svg>
    <div class="brand rise"><span class="mark"></span>RISE LEDGER</div>
    <div class="brand calm"><span class="mark"></span>calmfield works</div>
  </footer>

</main>
</body>
</html>
```